The Harvest Compass

Cutting Through the Noise to What Actually Works.

Nutrition book

Target Market(s)

People looking to be or get healthy and eat right.

```html
<!DOCTYPE html>
<html lang="en">
<head>
<meta charset="utf-8">
<title>The Harvest Compass</title>
<link href="https://fonts.googleapis.com/css2?family=Playfair+Display:wght@900&family=Montserrat:wght@400;500;700&family=Quicksand:wght@500&display=swap" rel="stylesheet">
<style>
  :root {
    --paper: #f6f5f1;
    --navy: #0f2340;
    --calories: #e9a81f;
    --protein: #2f7d32;
    --quality: #0b7a86;
    --timing: #4f7398;
    --supplements: #6a5b8c;
    --noise: #474c54;
    --white: #ffffff;
  }
  html, body {
    margin: 0;
    padding: 0;
    width: 800px;
    height: 1200px;
    overflow: hidden;
    background: var(--paper);
  }
  .cover {
    display: block;
    width: 800px;
    height: 1200px;
  }
  .title-rule { stroke: var(--navy); stroke-width: 1.6; }
  .title-kicker {
    font-family: "Montserrat", sans-serif;
    font-weight: 500;
    font-size: 40px;
    letter-spacing: 9px;
    fill: var(--navy);
  }
  .title-main {
    font-family: "Playfair Display", serif;
    font-weight: 900;
    font-size: 138px;
    fill: var(--navy);
  }
  .title-sub {
    font-family: "Montserrat", sans-serif;
    font-weight: 400;
    font-size: 86px;
    letter-spacing: 6px;
    fill: var(--navy);
  }
  .tagline {
    font-family: "Quicksand", sans-serif;
    font-weight: 500;
    font-size: 26px;
    fill: var(--navy);
  }
  .tier-label {
    font-family: "Montserrat", sans-serif;
    font-weight: 700;
    font-size: 23px;
    letter-spacing: 2px;
    fill: var(--white);
  }
  .tier-number-disc { fill: var(--white); }
  .tier-number {
    font-family: "Montserrat", sans-serif;
    font-weight: 700;
    font-size: 20px;
  }
  .icon-line {
    fill: none;
    stroke: var(--white);
    stroke-width: 3;
    stroke-linecap: round;
    stroke-linejoin: round;
  }
  .icon-solid { fill: var(--white); }
  .tier-calories { fill: var(--calories); }
  .tier-protein { fill: var(--protein); }
  .tier-quality { fill: var(--quality); }
  .tier-timing { fill: var(--timing); }
  .tier-supplements { fill: var(--supplements); }
  .tier-noise { fill: var(--noise); }
</style>
</head>
<body>
<svg class="cover" viewBox="0 0 800 1200" xmlns="http://www.w3.org/2000/svg">
  <!-- Title block -->
  <line class="title-rule" x1="156" y1="91" x2="313" y2="91"/>
  <line class="title-rule" x1="477" y1="91" x2="629" y2="91"/>
  <text class="title-kicker" x="400" y="106" text-anchor="middle">THE</text>
  <text class="title-main" x="400" y="224" text-anchor="middle" textLength="672" lengthAdjust="spacingAndGlyphs">HARVEST</text>
  <text class="title-sub" x="400" y="318" text-anchor="middle" textLength="560">COMPASS</text>
  <text class="tagline" x="400" y="372" text-anchor="middle">Cutting Through the Noise to What Actually Works</text>

  <!-- Tier 1: Calories -->
  <path class="tier-calories" d="M392 397 Q400 387 408 397 L526 543 Q532 551 522 551 L278 551 Q268 551 274 543 Z"/>
  <path class="icon-solid" d="M400 446 C412 458 421 468 417 481 C414 490 407 494 400 494 C391 494 383 488 383 478 C383 470 388 464 392 460 C392 466 395 470 398 471 C396 462 398 454 400 446 Z"/>
  <circle class="tier-number-disc" cx="328" cy="518" r="18"/>
  <text class="tier-number" x="328" y="525" text-anchor="middle" fill="var(--calories)">1</text>
  <text class="tier-label" x="422" y="526" text-anchor="middle">CALORIES</text>

  <!-- Tier 2: Protein -->
  <path class="tier-protein" d="M266 559 L535 559 Q541 559 543 565 L581 650 Q583 656 577 656 L223 656 Q217 656 219 650 L258 565 Q260 559 266 559 Z"/>
  <path class="icon-solid" d="M386 616 L386 600 C386 592 390 584 394 580 L397 576 C399 573 404 573 406 576 L408 581 L403 584 L401 583 L398 590 L400 598 C404 594 412 594 416 599 C419 603 419 611 416 616 Z"/>
  <circle class="tier-number-disc" cx="283" cy="604" r="18"/>
  <text class="tier-number" x="283" y="611" text-anchor="middle" fill="var(--protein)">2</text>
  <text class="tier-label" x="400" y="645" text-anchor="middle">PROTEIN</text>

  <!-- Tier 3: Food Quality -->
  <path class="tier-quality" d="M199 666 L601 666 Q607 666 609 672 L632 758 Q634 764 628 764 L172 764 Q166 764 168 758 L191 672 Q193 666 199 666 Z"/>
  <path class="icon-solid" d="M398 718 C384 716 372 706 374 688 C390 688 400 698 398 718 Z"/>
  <path class="icon-solid" d="M402 718 C406 698 414 684 426 680 C428 700 418 714 402 718 Z"/>
  <path class="icon-line" d="M400 720 L400 702"/>
  <circle class="tier-number-disc" cx="234" cy="713" r="18"/>
  <text class="tier-number" x="234" y="720" text-anchor="middle" fill="var(--quality)">3</text>
  <text class="tier-label" x="400" y="748" text-anchor="middle">FOOD QUALITY</text>

  <!-- Tier 4: Meal Timing -->
  <path class="tier-timing" d="M152 775 L648 775 Q654 775 656 781 L679 867 Q681 873 675 873 L125 873 Q119 873 121 867 L144 781 Q146 775 152 775 Z"/>
  <circle class="icon-line" cx="400" cy="810" r="20"/>
  <path class="icon-line" d="M400 797 L400 811 L409 818"/>
  <circle class="tier-number-disc" cx="189" cy="822" r="18"/>
  <text class="tier-number" x="189" y="829" text-anchor="middle" fill="var(--timing)">4</text>
  <text class="tier-label" x="400" y="858" text-anchor="middle">MEAL TIMING</text>

  <!-- Tier 5: Supplements -->
  <path class="tier-supplements" d="M113 884 L687 884 Q693 884 695 890 L717 976 Q719 982 713 982 L87 982 Q81 982 83 976 L105 890 Q107 884 113 884 Z"/>
  <g transform="rotate(-45 400 918)">
    <rect class="icon-line" x="380" y="909" width="40" height="18" rx="9"/>
    <path class="icon-line" d="M400 909 L400 927"/>
  </g>
  <circle class="tier-number-disc" cx="156" cy="931" r="18"/>
  <text class="tier-number" x="156" y="938" text-anchor="middle" fill="var(--supplements)">5</text>
  <text class="tier-label" x="400" y="967" text-anchor="middle">SUPPLEMENTS</text>

  <!-- Tier 6: Noise -->
  <path class="tier-noise" d="M74 993 L726 993 Q732 993 734 999 L757 1092 Q759 1098 753 1098 L47 1098 Q41 1098 43 1092 L66 999 Q68 993 74 993 Z"/>
  <path class="icon-line" d="M386 1012 L414 1012 Q422 1012 422 1020 L422 1032 Q422 1040 414 1040 L398 1040 L388 1048 L390 1040 L386 1040 Q378 1040 378 1032 L378 1020 Q378 1012 386 1012 Z"/>
  <circle class="icon-solid" cx="391" cy="1026" r="2.2"/>
  <circle class="icon-solid" cx="400" cy="1026" r="2.2"/>
  <circle class="icon-solid" cx="409" cy="1026" r="2.2"/>
  <circle class="tier-number-disc" cx="115" cy="1045" r="18"/>
  <text class="tier-number" x="115" y="1052" text-anchor="middle" fill="var(--noise)">6</text>
  <text class="tier-label" x="400" y="1078" text-anchor="middle">NOISE</text>
</svg>
</body>
</html>
```